The Lumo-Hub for Rescue Instruction + Venue Readiness Post Card

Hi! I am a new business that is Licensed Training Provider to the National Bluefield Aid. We teach private CPR/AED, First Aid and a variety of other emergency training courses to the general public! Our goal is to get into businesses of all sizes from the mom and pops store to corporate offices of Manhattan. We can do private classes in your home and no office space is to small! We even have a school assembly program that teaches "Hands Only CPR" for children. I'm looking to make a post card to hand out that can easily explain what we are doing…that might have some good visuals that catch your eye as well. I def want to use The Lumo Hub logo in it that I have attached. Im not necessarily married to any of the other images. You can check out our website www.lumohubinstruct.example for more information and you can use any of the images on there as well if you would like. I will give you free reign to find any cool photo stock image that you might think fits with what I'm trying to do. Hopefully you can help!
Updates

Also feel free to use any other photos that you might find that you think fit our cause for teaching CPR/First aid etc!! Thanks!

Thank you all for your hard work. I actually like many of these designs and really torn! I will be making some decisions in the next day or so. Thank you! Dale

Industry/Entity Type

Training

```html
<!DOCTYPE html>
<html lang="en">
<head>
<meta charset="utf-8">
<title>The Lumo-Hub Post Card</title>
<link href="https://fonts.googleapis.com/css2?family=Montserrat:wght@400;600;700;800;900&family=Open+Sans:wght@400;600;700&family=Roboto+Condensed:wght@400;700&display=swap" rel="stylesheet">
<style>
:root{
  --red:#e31e26;
  --dark:#231f20;
  --ink:#1a1a1a;
  --white:#ffffff;
  --stage:#e6e6e6;
  --orange:#f2682a;
  --head:'Montserrat',sans-serif;
  --body:'Open Sans',sans-serif;
  --cond:'Roboto Condensed',sans-serif;
}
*{margin:0;padding:0;box-sizing:border-box}
html,body{width:1200px;height:1000px;overflow:hidden;background:var(--stage)}
.card{position:absolute;background:var(--white);overflow:hidden;box-shadow:12px 14px 16px rgba(0,0,0,.35)}
.abs{position:absolute}

/* front card */
.front{left:157px;top:100px;width:479px;height:356px}
.front-header{left:0;top:0;width:479px;height:70px;background:var(--dark)}
.front-header-red{left:0;top:0;width:479px;height:70px;background:var(--red);clip-path:polygon(58% 0,100% 0,100% 100%,52% 100%)}
.brand{display:flex;flex-direction:column;align-items:flex-start}
.brand-name{display:flex;align-items:center;gap:6px;font-family:var(--head);font-weight:600;color:var(--white);letter-spacing:.5px;white-space:nowrap}
.brand-dot{width:9px;height:9px;background:var(--red);border-radius:50%}
.brand-tag{font-family:var(--head);font-weight:700;color:var(--orange);letter-spacing:.3px;white-space:nowrap}
.front .brand{left:26px;top:22px}
.front .brand-name{font-size:21px}
.front .brand-tag{font-size:5.5px;margin-left:84px;margin-top:2px}
.contact{left:282px;top:20px;display:flex;gap:7px;color:var(--white)}
.contact svg{width:16px;height:28px;margin-top:4px}
.contact-label{font-family:var(--head);font-weight:700;font-size:8px}
.contact-phone{font-family:var(--head);font-weight:800;font-size:15px;line-height:16px}
.contact-web{font-family:var(--head);font-weight:600;font-size:10px}
.hero{left:0;top:70px;width:479px;height:172px;background:linear-gradient(100deg,#2a2325 0%,#4b3b36 30%,#caa28a 48%,#d9b9a0 60%,#6a3e52 75%,#3a2a30 100%)}
.headline-small{left:16px;top:143px;font-family:var(--head);font-weight:800;font-size:17px;color:var(--white)}
.headline-big{left:14px;top:157px;font-family:var(--head);font-weight:900;font-size:72px;line-height:78px;color:var(--red);letter-spacing:-1px}
.intro{left:215px;top:198px;width:264px;height:42px;background:rgba(255,255,255,.82);padding:2px 15px 0 0;text-align:right;font-family:var(--head);font-weight:700;font-size:9.6px;line-height:13px;color:var(--ink)}
.intro b{color:var(--red)}
.caption-band{left:0;top:242px;width:479px;height:30px;background:var(--dark);color:var(--white);font-family:var(--head);font-weight:700;font-size:8.6px;padding:9px 0 0 16px}
.badge-art{left:12px;top:294px;width:62px;height:62px;background:radial-gradient(circle,#e8474d 0%,var(--red) 60%,#b7161d 100%);border-radius:50%}
.badge-line{left:53px;top:284px;font-family:var(--body);font-weight:700;font-size:10px;color:var(--ink);text-align:right;width:84px;line-height:12px}
.badge-line span{color:var(--red);font-weight:600}
.partner{left:88px;top:332px;display:flex;align-items:center;gap:4px;font-family:var(--body);font-weight:700;font-size:6px;line-height:7px;color:var(--ink);white-space:nowrap}
.partner-mark{width:12px;height:12px;background:var(--red);flex:none}
.ready{left:158px;top:286px;font-family:var(--body);font-weight:700;color:var(--red);font-size:14px;line-height:13px;text-align:center}
.ready .small{font-size:10px}
.ready .dark{color:var(--ink);font-size:11px}
.ready-art{left:148px;top:336px;width:116px;height:18px;background:linear-gradient(90deg,#333,#777,#333)}
.programs{left:0;top:272px;width:479px;height:84px;background:var(--red);clip-path:polygon(55.5% 0,100% 0,100% 100%,59% 100%)}
.programs-text{left:270px;top:285px;width:192px;font-family:var(--head);font-weight:700;font-size:8.6px;line-height:15px;color:var(--white);text-align:right}
.programs-text .title{text-align:left;margin-left:4px}
.programs-text .item{font-weight:600}

/* back card */
.back{left:484px;top:507px;width:476px;height:352px}
.back-red{left:0;top:0;width:476px;height:352px;background:var(--red);clip-path:polygon(311px 0,476px 0,476px 352px,252px 352px,266px 292px,221px 205px)}
.back-band{left:0;top:303px;width:270px;height:49px;background:var(--dark);clip-path:polygon(0 0,266px 0,252px 49px,0 49px)}
.back .brand{left:22px;top:314px}
.back .brand-name{font-size:22px}
.back .brand-tag{font-size:5.5px;margin-left:62px;margin-top:2px}
.about{left:17px;top:22px;width:262px;font-family:var(--body);font-size:9.6px;line-height:11.6px;letter-spacing:.25px;color:var(--ink)}
.about b{color:var(--red)}
.services-title{left:17px;top:121px;font-family:var(--body);font-weight:700;font-size:9.6px;color:var(--red)}
.services{left:20px;top:135px;list-style:none;font-family:var(--body);font-size:9.6px;line-height:11.6px;letter-spacing:.25px;color:var(--ink)}
.services li{padding-left:13px;position:relative}
.services li::before{content:"+";position:absolute;left:0;top:-1px;color:var(--red);font-weight:700;font-size:12px}
.portrait{left:352px;top:23px;width:96px;height:142px;background:linear-gradient(180deg,#b9b8b5 0%,#8e7f73 40%,#3d4450 100%)}
.bio{left:230px;top:170px;width:218px;text-align:right;font-family:var(--cond);font-size:10px;line-height:12.4px;color:var(--white)}
.bio b{font-size:12px}
.booking{left:280px;top:253px;width:168px;text-align:right;font-family:var(--head);font-weight:700;font-size:8.6px;line-height:11px;color:var(--white)}
.owner{left:260px;top:293px;width:188px;text-align:right;font-family:var(--body);font-size:11px;line-height:13px;color:var(--white)}
.owner b{font-family:var(--head);font-weight:800;font-size:11.5px}
</style>
</head>
<body>

<section class="card front" aria-label="Post card front">
  <div class="abs front-header"></div>
  <div class="abs front-header-red"></div>
  <div class="abs brand">
    <div class="brand-name">THE LUMO HUB<span class="brand-dot"></span></div>
    <div class="brand-tag">RESCUE INSTRUCTION + VENUE READINESS</div>
  </div>
  <div class="abs contact">
    <svg viewBox="0 0 16 28" aria-hidden="true"><path d="M4 1h4l1 7-3 2c1 4 2 6 4 9l3-2 3 6-3 3C7 26 2 15 1 5z" fill="#fff"/></svg>
    <div>
      <div class="contact-label">CONTACT US TODAY:</div>
      <div class="contact-phone">+1 555-014-2290</div>
      <div class="contact-web">www.lumohubinstruct.example</div>
    </div>
  </div>

  <div class="abs hero" role="img" aria-label="Photo of gloved hands giving CPR to a training manikin with a breathing mask"></div>
  <div class="abs headline-small">LEARN TO SAVE A</div>
  <div class="abs headline-big">LIFE</div>
  <p class="abs intro"><b>THE LUMO-HUB</b> IS A LEADING PROVIDER OF SAFETY AND EMERGENCY PREPAREDNESS TRAINING + EVENT SAFETY MANAGENT</p>
  <div class="abs caption-band">LEARN HOW TO SAVE A LIFE TODAY IN OUR VARIETY OF EMERGENCY PREPARATION COURSES!</div>

  <div class="abs badge-art" role="img" aria-label="Red globe illustration"></div>
  <div class="abs badge-line">Get CPR trained.<br><span>Save a life.</span></div>
  <div class="abs partner"><span class="partner-mark"></span><span>National<br>Bluefield Aid</span></div>
  <div class="abs ready">Ready <span class="small">for an</span><br>Emergency?<br><span class="dark">You can be.</span></div>
  <div class="abs ready-art" role="img" aria-label="Row of small disaster scene illustrations"></div>

  <div class="abs programs"></div>
  <div class="abs programs-text">
    <div class="title">SPECIALIZED PROGRAMS FOR SCHOOLS:</div>
    <div class="item">- FIRST AID FOR STUDENT</div>
    <div class="item">- CPR FOR STUDENTS</div>
    <div class="item">- FIRST AID AND CPR FOR STUDENT</div>
  </div>
</section>

<section class="card back" aria-label="Post card back">
  <div class="abs back-red"></div>
  <div class="abs back-band"></div>
  <div class="abs brand">
    <div class="brand-name">THE LUMO HUB<span class="brand-dot"></span></div>
    <div class="brand-tag">RESCUE INSTRUCTION + VENUE READINESS</div>
  </div>

  <p class="abs about"><b>THE LUMO-HUB</b> for Rescue Instruction &amp; Consulting is a Limited Liability Corporation organized under the laws of the State of New York. Our highly qualified instructors &amp; independent contractors hold numerous certifications &amp; licenses from various Government Agencies and Organizations. We take pride in our services, &amp; hold ourselves to the highest level of professionalism for all events.</p>
  <div class="abs services-title">SERVICE WE PROVIDE:</div>
  <ul class="abs services">
    <li>National Certification in variety of CPR<br>/AED / FIRST AID / O2 Courses</li>
    <li>National Bluefield Aid Lifeguard Training</li>
    <li>Lifeguards for all events</li>
    <li>Rescue board rentals</li>
    <li>Marine safety coordination</li>
    <li>Certified rescue drivers</li>
    <li>Communication rentals</li>
    <li>Customized emergency action plans</li>
    <li>First AID kits / Supplies</li>
    <li>Athletic trainers</li>
    <li>Safety walk throughs</li>
    <li>Fireguards</li>
  </ul>

  <div class="abs portrait" role="img" aria-label="Portrait photo of the founder seated, in a dark sweater"></div>
  <p class="abs bio">owner and founder of the <b>THE LUMO-HUB,<br>DALE MARWICK</b> is an expert in his field. 17 Years as a emergency medical technician and ocean lifeguard with the perstigious HARBOR POINT LIFEGUARD CORPS, Dale brings a wealth of knowledge and experience to all of his clients.</p>
  <p class="abs booking">FOR MORE INFORMATION ON BOOKING THE LUMO-HUB FOR YOUR EVENT, CONTACT:</p>
  <p class="abs owner"><b>DALE MARWICK</b><br>P: +1 555-014-2290<br>E: lumohub911@mailbox.example<br>www.lumohubinstruct.example</p>
</section>

</body>
</html>
```